New York College Admissions Consulting Company Looking for a One-Page Flyer Design

We are a college admissions consulting company Brackwell Admissions Consulting (www.brackwelladmissions.example) and we help students apply to universities. We need a 1-page flyer design to hand out at a science competition for high school students. I attach all the information that should be included in the flyer and the logo. Please make a stylistic and professional looking flyer, which will impress these very smart and sophisticated high school students and even more importantly - their parents. Feel free to move the text around the flyer and to change the font as you see fit. Also, please add a stock picture or two, as you see fit. Also, let me know if I have to pay for the stock photos (if I have to get a license to use the photos on the flyer), and where and how much I would need to pay.

Target Market(s)

Smart and sophisticated high school students and even more importantly - their parents.

Industry/Entity Type

College

Requirements
Must have
• Must look sophisticated. This is an expensive service and parents need to know that our image matches our prices.
Should not have
• Wild colors like red.

```html
<!DOCTYPE html>
<html lang="en">
<head>
<meta charset="utf-8">
<title>Complimentary Live Online Class – Brackwell Admissions Consulting</title>
<link rel="stylesheet" href="https://fonts.googleapis.com/css2?family=Cinzel:wght@700&family=PT+Sans+Narrow:wght@700&family=Source+Sans+3:wght@300;400;600&display=swap">
<style>
  :root {
    --stage: #1c1c1c;
    --paper: #ffffff;
    --blue-deep: #0f5fb3;
    --blue-mid: #2a8ad6;
    --blue-sky: #5fbdf0;
    --blue-badge: #0d6cb6;
    --blue-tag: #4bb3e8;
    --blue-head: #1262ae;
    --text-grey: #5b5b5b;
    --tick-green: #6cb33f;
    --rule: #7ccaf0;
  }
  * { box-sizing: border-box; margin: 0; padding: 0; }
  html, body { width: 1200px; height: 1000px; overflow: hidden; }
  body { background: var(--stage); position: relative; font-family: "Source Sans 3", sans-serif; }

  .flyer {
    position: absolute; left: 306px; top: 92px;
    width: 589px; height: 811px;
    background: var(--paper); overflow: hidden;
  }
  .flyer-header {
    position: absolute; left: 0; top: 0; width: 589px; height: 460px;
    background: linear-gradient(180deg, var(--blue-deep) 0%, var(--blue-mid) 30%, var(--blue-sky) 52%, #bfe6fa 72%, #ffffff 92%);
  }
  .wave-band {
    position: absolute; left: 0; top: 180px; width: 589px; height: 230px;
    background: linear-gradient(180deg, rgba(255,255,255,0) 0%, rgba(40,130,210,.35) 45%, rgba(255,255,255,.55) 80%, rgba(255,255,255,0) 100%);
  }
  .student-photo {
    position: absolute; left: 161px; top: 140px; width: 266px; height: 266px;
    border-radius: 50%;
    background: linear-gradient(180deg, #c9b867 0%, #7f9a46 45%, #4f8a2e 100%);
  }

  .headline {
    position: absolute; left: 0; top: 22px; width: 589px;
    text-align: center; color: #fff;
    font-family: "Cinzel", serif; font-weight: 700;
    font-size: 38px; line-height: 41px;
    text-shadow: 0 2px 4px rgba(0,0,0,.25);
  }
  .session-title {
    position: absolute; left: 113px; top: 112px; width: 361px; height: 18px;
    background: #fff; color: var(--blue-badge);
    font-size: 13px; line-height: 18px; text-align: center; font-weight: 400;
  }
  .time-badge, .date-badge {
    position: absolute; width: 92px; height: 92px; border-radius: 50%;
    background: var(--blue-badge); color: #fff; text-align: center;
    display: flex; flex-direction: column; justify-content: center;
  }
  .time-badge { left: 116px; top: 319px; font-size: 15px; line-height: 19px; }
  .date-badge { left: 381px; top: 319px; font-size: 14px; line-height: 17px; }
  .date-badge .date-day { font-size: 20px; font-weight: 600; line-height: 22px; }
  .live-tag {
    position: absolute; left: 193px; top: 416px; width: 203px; height: 17px;
    background: var(--blue-tag); color: #fff;
    font-size: 14px; line-height: 17px; text-align: center;
  }

  .section-heading {
    position: absolute; left: 18px;
    font-family: "PT Sans Narrow", sans-serif; font-weight: 700;
    font-size: 19px; color: var(--blue-head);
  }
  .learn-heading { top: 460px; }
  .facts-heading { top: 560px; left: 21px; }
  .checklist { position: absolute; left: 18px; width: 560px; list-style: none; }
  .checklist li {
    position: relative; padding-left: 13px;
    font-size: 11px; line-height: 17.5px; color: var(--text-grey);
  }
  .checklist li::before {
    content: ""; position: absolute; left: 1px; top: 5px;
    width: 7px; height: 4px;
    border-left: 2px solid var(--tick-green); border-bottom: 2px solid var(--tick-green);
    transform: rotate(-45deg);
  }
  .learn-list { top: 487px; }
  .facts-list { top: 588px; }

  .footer-rule {
    position: absolute; left: 20px; top: 730px; width: 548px;
    border-top: 1px dashed var(--rule);
  }
  .brand {
    position: absolute; left: 20px; top: 758px;
    display: flex; align-items: center; gap: 9px;
  }
  .brand-mark { width: 28px; height: 28px; border-radius: 50%; background: var(--blue-mid); }
  .brand-name {
    font-size: 19px; font-weight: 400; color: var(--blue-badge); line-height: 22px; white-space: nowrap;
  }
  .contact { position: absolute; right: 27px; top: 745px; text-align: right; }
  .contact-phone { font-size: 26px; font-weight: 300; color: var(--blue-badge); line-height: 30px; letter-spacing: -.3px; }
  .contact-web {
    font-size: 11px; color: var(--blue-badge); line-height: 14px;
    border-top: 1px dotted var(--rule); padding-top: 2px;
  }
</style>
</head>
<body>
<article class="flyer">
  <div class="flyer-header"></div>
  <div class="wave-band" role="img" aria-label="Decorative blue and white wave swooshes"></div>
  <div class="student-photo" role="img" aria-label="Photo of a smiling student lying on the grass reading a book"></div>

  <h1 class="headline">Complimentary Live<br>Online Class</h1>
  <p class="session-title">“The College Personal Statement and Perfecting Your Narrative”</p>

  <div class="time-badge"><span>4 pm to</span><span>5 pm EST</span></div>
  <div class="date-badge"><span>Sunday</span><span class="date-day">May 31</span><span>2015</span></div>
  <p class="live-tag">Live Answers to Live Questions</p>

  <h2 class="section-heading learn-heading">Learn How To:</h2>
  <ul class="checklist learn-list">
    <li>Avoid the Most Common Mistakes Made in The Personal Statement</li>
    <li>Compose a Memorable Essay</li>
    <li>Craft a Compelling Narrative</li>
  </ul>

  <h2 class="section-heading facts-heading">Admission Facts and Tips:</h2>
  <ul class="checklist facts-list">
    <li>In the last 9 years, the Average Ivy League College Admission Rate has dropped by 49%.</li>
    <li>Admission Rate in 2005 - 17.1%</li>
    <li>Admission Rate in 2014 - 8.8%</li>
    <li>The Personal Statement and the Supplemental Essays comprise approximately 25% of the admission criteria.</li>
    <li>Crafting the Perfect Narrative is vital to your college application. It can mean the difference between an acceptance and a rejection.</li>
  </ul>

  <div class="footer-rule"></div>
  <div class="brand">
    <span class="brand-mark"></span>
    <span class="brand-name">Brackwell Admissions Consulting</span>
  </div>
  <div class="contact">
    <p class="contact-phone">1.212.555.0148</p>
    <p class="contact-web">www.brackwelladmissions.example</p>
  </div>
</article>
</body>
</html>
```